Get me out of Jail business cards!!!!

I need business cards done for my business. I own a BailBonds and I get people out of jail!

Colors are red white and black

I need it to say on the card these details:

Rollin’ Free Bailbonds

452 S Kettering Ave
Arcadia, FL 34266

863-555-0172

Open 24/7

On the back of the card:

Must check in every Tuesday.

______/______/______ court date
____________________ time
You must know your court date at all times!

Marla Tisdell - owner
Rosalind Tisdell - agent
Denise Crandon - agent

Industry/Entity Type

Bail bonds

Contact Information for Business Card

Colors are red white and black I need it to say on the card these details: Rollin’ Free Bailbonds 452 S Kettering Ave Arcadia, FL 34266 863-555-0172 Open 24/7 On the back of the card: Must check in every Tuesday. ______/______/______ court date ____________________ time You must know your court date at all times! Marla Tisdell - owner Rosalind Tisdell - agent Denise Crandon - agent

Font styles to use
Serif
Sans Serif

Colors
EB3D1F
EC4F4E
F09395
F8D3D4
FCEDEE

Requirements
Must have
• I listed the must haves in the business card details
Nice to have
• Handcuffs or jail bars or a man in a black and white suit

```html
<!DOCTYPE html>
<html lang="en">
<head>
<meta charset="utf-8">
<title>Rollin’ Free Bailbonds – Business Card</title>
<link href="https://fonts.googleapis.com/css2?family=Poppins:wght@400;500&display=swap" rel="stylesheet">
<style>
  :root {
    --backdrop: #2b2b2b;
    --ink: #000000;
    --paper: #ffffff;
    --alert-red: #ff0000;
    --heading-ink: #1e1e1e;
    --label-ink: #454545;
  }
  * { margin: 0; padding: 0; box-sizing: border-box; }
  html, body {
    width: 1093px; height: 1200px; overflow: hidden;
    background: var(--backdrop);
    font-family: "Poppins", sans-serif;
  }
  .card {
    position: absolute;
    left: 265px;
    width: 580px;
    height: 358px;
    border-radius: 26px;
    overflow: hidden;
  }
  /* Front */
  .card-front { top: 226px; background: var(--ink); color: var(--paper); }
  .hours {
    position: absolute; top: 38px; left: 0; right: 0;
    text-align: center; color: var(--alert-red);
    font-size: 21px; font-weight: 500;
  }
  .business-name {
    position: absolute; top: 100px; left: 0; right: 0;
    text-align: center; font-weight: 400; line-height: 1;
  }
  .business-name .line-small { display: block; font-size: 36px; }
  .business-name .line-large { display: block; font-size: 72px; margin-top: 6px; letter-spacing: 1px; }
  .address {
    position: absolute; left: 43px; top: 270px;
    font-size: 17px; line-height: 21px;
  }
  .phone {
    position: absolute; right: 42px; top: 286px;
    font-size: 22px; font-weight: 500; letter-spacing: 0.5px;
  }
  /* Back */
  .card-back { top: 621px; background: var(--paper); }
  .reminder {
    position: absolute; top: 48px; left: 0; right: 0; text-align: center;
    font-size: 21px; font-weight: 500; color: var(--heading-ink);
  }
  .field {
    position: absolute; left: 0; right: 0; text-align: center;
    font-size: 17px; color: var(--label-ink); white-space: nowrap;
  }
  .field-date { top: 108px; }
  .field-time { top: 150px; }
  .field .blank { letter-spacing: 1.5px; margin-left: 4px; }
  .warning {
    position: absolute; top: 194px; left: 0; right: 0; text-align: center;
    font-size: 17.5px; font-weight: 500; color: var(--alert-red);
  }
  .staff-band {
    position: absolute; left: 0; right: 0; top: 245px; bottom: 0;
    background: var(--ink);
  }
  .staff {
    position: absolute; top: 35px; width: 200px; margin-left: -100px;
    text-align: center; line-height: 21px;
  }
  .staff-name { display: block; color: var(--paper); font-size: 17.5px; font-weight: 500; }
  .staff-role { display: block; color: var(--alert-red); font-size: 17.5px; }
  .staff-owner { left: 113px; }
  .staff-agent-one { left: 307px; }
  .staff-agent-two { left: 487px; }
</style>
</head>
<body>
  <section class="card card-front">
    <p class="hours">Open 24/7</p>
    <h1 class="business-name">
      <span class="line-small">Rollin’ Free</span>
      <span class="line-large">Bailbonds</span>
    </h1>
    <p class="address">452 S Kettering Ave<br>Arcadia, FL 34266</p>
    <p class="phone">863-555-0172</p>
  </section>

  <section class="card card-back">
    <p class="reminder">Must check in every Tuesday.</p>
    <p class="field field-date">Court date: <span class="blank">______/______/______</span></p>
    <p class="field field-time">Time: <span class="blank">_____________________</span></p>
    <p class="warning">You must know your court date at all times!</p>
    <div class="staff-band">
      <div class="staff staff-owner"><span class="staff-name">Marla Tisdell</span><span class="staff-role">Owner</span></div>
      <div class="staff staff-agent-one"><span class="staff-name">Rosalind Tisdell</span><span class="staff-role">Agent</span></div>
      <div class="staff staff-agent-two"><span class="staff-name">Denise Crandon</span><span class="staff-role">Agent</span></div>
    </div>
  </section>
</body>
</html>
```